Blue Harbor Car Finance Home Page

We need a desktop version mock up (we will base our mobile version off of this) of a website homepage for our auto loan business, Blue Harbor Car Finance. This does not need to be a functioning site, just a home page mock up. We are based in the metro St. Louis, MO area. We offer "guaranteed" auto loans for all credit types. We specialize in financing for bad/no credit customers. We are able to help rebuild these type of customers' credit, all while putting them in a great late model vehicle they'll love. Our online credit app takes less than 60 seconds, doesn't require a SS# and gives a free credit score if they fill it out within 3 minutes. We are looking for an outside perspective to help us in this design process. We are not completely sure what we want, but we do want it to be professional and secure looking, all while being unique and aesthetically pleasing. We want the customer to be able to put in their zip code to be directed to the right location that can get them pre approved. I attached a wireframe with some stuff we'd like to include, but in no way does it have to be in the same layout or the same ideas. We want everyone to "go crazy" with their creative side on this. Our current site is awful, here is a link to get a better idea: www.blueharborcarfinance-example.com. Attached is our logo too, base colors off of it. Watch our video that is also attached for a better idea.

Target Market(s)

Residents of the St. Louis Missouri Metro Area that need an auto loan. 24-55 Male and Female - Lots of "urban market" customers.

Industry/Entity Type

Loan

Number of Pages Required

1 page

Colors
9bcb3b

Requirements
Must have
• An area where the customer can enter their zip code - Be creative!
Nice to have
• See wireframe attachment for ideas - Be creative!

```html
<!DOCTYPE html>
<html lang="en">
<head>
<meta charset="utf-8">
<title>Blue Harbor Car Finance – Mobile Home</title>
<link rel="stylesheet" href="https://fonts.googleapis.com/css2?family=Saira+Semi+Condensed:wght@400;600;700&family=Noto+Serif:ital,wght@1,400;1,700&display=swap">
<style>
  :root {
    --page-bg: #ececec;
    --header-bg: #1b1b1b;
    --hero-dark: #2a2d33;
    --hero-mid: #4a4f58;
    --accent-orange: #e35a1c;
    --accent-yellow: #fdc300;
    --brand-green: #76b82a;
    --bullet-green: #8fcf3a;
    --text-white: #ffffff;
    --text-dark: #1f2a36;
    --input-placeholder: #b5b5b5;
  }
  * { box-sizing: border-box; margin: 0; padding: 0; }
  html, body { width: 1200px; height: 1000px; overflow: hidden; }
  body {
    background: var(--page-bg);
    font-family: "Saira Semi Condensed", sans-serif;
    position: relative;
  }
  .screen {
    position: absolute;
    left: 319px; top: 14px;
    width: 562px; height: 972px;
    overflow: hidden;
    background: var(--header-bg);
  }
  .site-header {
    position: relative;
    height: 86px;
    background: var(--header-bg);
    display: flex; align-items: center; justify-content: space-between;
    padding: 0 22px;
  }
  .icon-button {
    width: 42px; height: 40px;
    border: 2px solid var(--accent-yellow);
    border-radius: 3px;
    display: flex; align-items: center; justify-content: center;
  }
  .brand {
    display: flex; align-items: center; gap: 10px;
  }
  .brand-square {
    width: 40px; height: 40px; background: var(--accent-yellow);
  }
  .brand-name {
    color: var(--brand-green);
    font-weight: 700;
    font-size: 22px;
    line-height: 21px;
    text-transform: uppercase;
  }
  .hero {
    position: relative;
    height: 604px;
  }
  .hero-photo {
    position: absolute; inset: 0;
    background:
      radial-gradient(ellipse at 45% 40%, #6b5a55 0%, transparent 45%),
      linear-gradient(180deg, var(--hero-mid) 0%, var(--hero-dark) 60%, #202226 100%);
    opacity: .9;
  }
  .hero-content { position: relative; text-align: center; padding-top: 50px; }
  .hero-title {
    color: var(--accent-orange);
    font-weight: 600;
    font-size: 40px;
    line-height: 46px;
  }
  .hero-tagline {
    font-family: "Noto Serif", serif;
    font-style: italic; font-weight: 700;
    color: var(--text-white);
    font-size: 18px; margin-top: 4px;
  }
  .benefits {
    list-style: none;
    text-align: left;
    margin: 28px 0 0 153px;
  }
  .benefits li {
    color: var(--bullet-green);
    font-size: 18px; line-height: 27px;
    display: flex; align-items: center; gap: 15px;
  }
  .benefits li::before {
    content: ""; width: 15px; height: 15px;
    background: var(--accent-yellow); border-radius: 2px;
  }
  .zip-panel {
    position: absolute;
    left: 69px; top: 362px;
    width: 447px; height: 201px;
    background: var(--accent-yellow);
    border-radius: 5px;
    padding: 37px 70px 0;
  }
  .zip-input {
    display: block; width: 100%; height: 53px;
    background: var(--text-white);
    border: 1px solid #d9d9d9; border-radius: 3px;
    font-family: inherit; font-size: 22px;
    color: var(--input-placeholder);
    padding: 0 16px; line-height: 51px;
  }
  .zip-submit {
    display: block; width: 100%; height: 51px; margin-top: 18px;
    background: var(--brand-green); color: var(--text-white);
    border-radius: 2px;
    font-size: 23px; text-align: center; line-height: 51px;
  }
  .testimonial {
    position: relative;
    height: 282px;
    background: var(--brand-green);
    text-align: center;
    padding-top: 30px;
  }
  .testimonial-label {
    color: var(--text-dark);
    font-weight: 600; font-size: 17px; letter-spacing: .5px;
  }
  .testimonial-quote {
    font-family: "Noto Serif", serif; font-style: italic;
    color: var(--text-white);
    font-size: 15.5px; line-height: 19px;
    text-align: justify;
    width: 357px; margin: 14px auto 0;
  }
  .testimonial-author {
    font-family: "Noto Serif", serif; font-style: italic;
    color: var(--text-dark); font-size: 15.5px; margin-top: 14px;
  }
  .carousel-arrow { position: absolute; top: 106px; }
  .carousel-arrow.prev { left: 28px; }
  .carousel-arrow.next { right: 28px; }
  .scroll-down {
    position: absolute; left: 50%; bottom: -62px;
    width: 124px; height: 124px; margin-left: -62px;
    border-radius: 50%; background: var(--accent-yellow);
  }
  .scroll-down svg { position: absolute; left: 44px; top: 20px; }
</style>
</head>
<body>
  <main class="screen">
    <header class="site-header">
      <div class="icon-button" aria-label="Menu">
        <svg width="26" height="18" viewBox="0 0 26 18"><rect y="0" width="26" height="3" fill="#fdc300"/><rect y="7.5" width="26" height="3" fill="#fdc300"/><rect y="15" width="26" height="3" fill="#fdc300"/></svg>
      </div>
      <div class="brand">
        <span class="brand-square"></span>
        <span class="brand-name">Blue Harbor<br>Car Finance</span>
      </div>
      <div class="icon-button" aria-label="Call us">
        <svg width="20" height="22" viewBox="0 0 24 24"><path fill="#fdc300" d="M6.6 10.8c1.4 2.8 3.8 5.1 6.6 6.6l2.2-2.2c.3-.3.7-.4 1-.2 1.1.4 2.3.6 3.6.6.6 0 1 .4 1 1V20c0 .6-.4 1-1 1C10.6 21 3 13.4 3 4c0-.6.4-1 1-1h3.5c.6 0 1 .4 1 1 0 1.3.2 2.5.6 3.6.1.3 0 .7-.2 1l-2.3 2.2z"/></svg>
      </div>
    </header>

    <section class="hero">
      <div class="hero-photo" role="img" aria-label="Blurred photo of a hand holding car keys in front of a vehicle"></div>
      <div class="hero-content">
        <h1 class="hero-title">Over 30,000<br>Auto Loans Since 2000</h1>
        <p class="hero-tagline">Pre-Approval in Under 60 Seconds!</p>
        <ul class="benefits">
          <li>No Social Security Number Required</li>
          <li>Instant Approval</li>
          <li>No Application Fees</li>
          <li>All Credit Accepted</li>
        </ul>
      </div>
      <form class="zip-panel">
        <span class="zip-input">Enter your zip code</span>
        <span class="zip-submit">Get Approved</span>
      </form>
    </section>

    <section class="testimonial">
      <h2 class="testimonial-label">TESTIMONIAL</h2>
      <p class="testimonial-quote">Lorem ipsum dolor sit amet, consectetur adipiscing elit, sed do eiusmod tempor incididunt ut labore et dolore magna aliqua. Ut enim ad minim veniam, quis nostrud exercitation ullamco laboris nisi ut aliquip ex ea commodo consequat.</p>
      <p class="testimonial-author">Sam Porter - Hartford, Connecticut</p>
      <svg class="carousel-arrow prev" width="20" height="38" viewBox="0 0 20 38"><polyline points="18,2 2,19 18,36" fill="none" stroke="#ffffff" stroke-width="2"/></svg>
      <svg class="carousel-arrow next" width="20" height="38" viewBox="0 0 20 38"><polyline points="2,2 18,19 2,36" fill="none" stroke="#ffffff" stroke-width="2"/></svg>
      <div class="scroll-down" aria-label="Scroll down">
        <svg width="36" height="14" viewBox="0 0 36 14"><polygon points="0,0 36,0 18,14" fill="#1f2a36"/></svg>
      </div>
    </section>
  </main>
</body>
</html>
```